School Management website

I need page design for our school management system website

Base website is www.tavrinel.com. When the student logs in, he will reach the below pages.
You can either design with white and blue background or grey and white background

Page 1 - School Info

Header
product name("Tavrinel") in left corner
logout link in right corner

LeftMenu

Dashboard
School Info
School Settings
Staffs
Classes
Messaging
Contact Us

Footer
About link and copyright text

School Info content
The page should have breadcrumb

The content of this page will be the school profile
We have to show the school logo
Name
School Type
School Code
School Count
School Address
School phone 1&2
School Email
School Website

The page content should show edit school profile link which will take the user to another page

```html
<!DOCTYPE html>
<html lang="en">
<head>
<meta charset="utf-8">
<title>Tavrinel – School Info</title>
<link rel="stylesheet" href="https://fonts.googleapis.com/css2?family=Arimo:wght@400;700&display=swap">
<style>
  :root {
    --brand-blue: #1d9bfc;
    --ink: #111111;
    --rule: #d8d8d8;
    --logo-border: #cfcfcf;
    --logo-text: #bdbdbd;
    --footer-bg: #444444;
    --white: #ffffff;
  }
  * { box-sizing: border-box; margin: 0; padding: 0; }
  html, body { width: 1200px; height: 1022px; overflow: hidden; background: var(--white); }
  body { position: relative; font-family: "Arimo", Arial, sans-serif; color: var(--ink); }

  .site-header { position: absolute; left: 0; top: 0; width: 1200px; height: 77px; background: var(--brand-blue); }
  .brand-name { position: absolute; left: 20px; top: 12px; font-size: 48px; font-weight: 700; color: var(--white); line-height: 1; }
  .logout-link { position: absolute; right: 14px; top: 11px; font-size: 17px; color: var(--white); text-decoration: none; }

  .breadcrumb { position: absolute; left: 0; top: 77px; width: 1200px; height: 33px; border-bottom: 1px solid var(--rule); font-size: 18px; }
  .breadcrumb span { position: absolute; top: 7px; }
  .crumb-home { left: 14px; }
  .crumb-sep { left: 84px; }
  .crumb-current { left: 113px; }

  .content-panel { position: absolute; left: 114px; top: 151px; width: 1033px; height: 738px; border: 2px solid var(--brand-blue); }
  .panel-title { position: absolute; left: 0; top: 0; width: 100%; height: 71px; background: var(--brand-blue); color: var(--white); font-size: 36px; font-weight: 400; padding: 16px 0 0 13px; letter-spacing: -0.5px; }

  .side-menu { position: absolute; left: 0; top: 194px; width: 175px; height: 314px; background: var(--brand-blue); }
  .side-menu a { position: absolute; left: 7px; font-size: 22px; color: var(--white); text-decoration: none; line-height: 1; }
  .side-menu a.is-current { text-decoration: underline; text-underline-offset: 3px; }
  .menu-toggle { position: absolute; left: 157px; top: 133px; }

  .profile-table { position: absolute; left: 186px; top: 0; width: 650px; }
  .profile-row { position: absolute; left: 0; width: 650px; border-bottom: 1px solid var(--rule); }
  .profile-label { position: absolute; left: 2px; font-size: 18px; color: var(--ink); }
  .profile-value { position: absolute; left: 156px; font-size: 19px; letter-spacing: -0.2px; color: var(--brand-blue); line-height: 39px; width: 490px; }

  .school-logo { position: absolute; left: 858px; top: 202px; width: 204px; height: 237px; background: var(--white); border: 2px solid var(--logo-border); display: flex; align-items: center; justify-content: center; font-size: 22px; color: var(--logo-text); }
  .logo-caption { position: absolute; left: 912px; top: 450px; font-size: 18px; }
  .logo-change { font-size: 11px; margin-left: 10px; vertical-align: 2px; }

  .edit-profile { position: absolute; left: 686px; top: 770px; width: 150px; height: 41px; border: 2px solid var(--brand-blue); font-size: 15px; font-weight: 700; color: var(--ink); text-decoration: none; display: flex; align-items: center; justify-content: center; background: var(--white); }

  .site-footer { position: absolute; left: 0; top: 955px; width: 1200px; height: 67px; background: var(--footer-bg); color: var(--white); font-size: 15px; font-weight: 700; }
  .site-footer span, .site-footer svg { position: absolute; }
  .copyright { left: 19px; top: 24px; }
  .footer-phone { left: 846px; top: 26px; }
  .footer-email { left: 1031px; top: 24px; }
</style>
</head>
<body>
  <header class="site-header">
    <div class="brand-name">Tavrinel</div>
    <a class="logout-link" href="#">Logout</a>
  </header>

  <nav class="breadcrumb">
    <span class="crumb-home">Home</span>
    <span class="crumb-sep">&#x203A;</span>
    <span class="crumb-current">School info</span>
  </nav>

  <main class="content-panel">
    <h1 class="panel-title">School Info</h1>
  </main>

  <div class="profile-table">
    <div class="profile-row" style="top:253px;height:39px"><span class="profile-label" style="top:10px">School Name</span><span class="profile-value">Lorem ipsum dolor sit amet, consectetur adipiscing elit</span></div>
    <div class="profile-row" style="top:303px;height:45px"><span class="profile-label" style="top:10px">School Type</span><span class="profile-value">Praesent vel varius turpis</span></div>
    <div class="profile-row" style="top:355px;height:45px"><span class="profile-label" style="top:10px">School Code</span><span class="profile-value">001</span></div>
    <div class="profile-row" style="top:406px;height:42px"><span class="profile-label" style="top:10px">School Count</span></div>
    <div class="profile-row" style="top:454px;height:96px"><span class="profile-label" style="top:11px">School Address</span><span class="profile-value">Sed ac orci et lorem sollicitudin viverra phasellus pretium consectetur turpis et gravida dui lacinia sed. Cras</span></div>
    <div class="profile-row" style="top:553px;height:42px"><span class="profile-label" style="top:10px">School Phone 1</span><span class="profile-value">XXX XXX XXXX</span></div>
    <div class="profile-row" style="top:600px;height:42px"><span class="profile-label" style="top:10px">School Phone 2</span><span class="profile-value">XXX XXX XXXX</span></div>
    <div class="profile-row" style="top:645px;height:44px"><span class="profile-label" style="top:10px">School Email</span><span class="profile-value">info@xxxxxx.com</span></div>
    <div class="profile-row" style="top:692px;height:42px"><span class="profile-label" style="top:10px">School Website</span><span class="profile-value">schoolxxxxxx.com</span></div>
  </div>

  <div class="school-logo" role="img" aria-label="School logo placeholder">Logo</div>
  <div class="logo-caption">School Logo<span class="logo-change">[Change]</span></div>

  <a class="edit-profile" href="#">Edit School Profile</a>

  <nav class="side-menu">
    <a class="is-current" href="#" style="top:11px">Dashboard</a>
    <a href="#" style="top:53px">School Info</a>
    <a href="#" style="top:96px">School Setting</a>
    <a href="#" style="top:143px">Staffs</a>
    <a href="#" style="top:187px">Classes</a>
    <a href="#" style="top:231px">Messaging</a>
    <a href="#" style="top:279px">Contact Us</a>
    <svg class="menu-toggle" width="10" height="26" viewBox="0 0 10 26"><polyline points="9,1 1,13 9,25" fill="none" stroke="#ffffff" stroke-width="1.5"/></svg>
  </nav>

  <footer class="site-footer">
    <span class="copyright">Copyright © 2014 | All Rights Reserved</span>
    <svg style="left:826px;top:27px" width="15" height="15" viewBox="0 0 24 24"><path fill="#ffffff" d="M6.6 10.8a15.1 15.1 0 0 0 6.6 6.6l2.2-2.2c.3-.3.7-.4 1-.2 1.1.4 2.3.6 3.6.6.6 0 1 .4 1 1V20c0 .6-.4 1-1 1A17 17 0 0 1 3 4c0-.6.4-1 1-1h3.5c.6 0 1 .4 1 1 0 1.3.2 2.5.6 3.6.1.3 0 .7-.2 1z"/></svg>
    <span class="footer-phone">+91 90210 47316</span>
    <svg style="left:1002px;top:27px" width="17" height="13" viewBox="0 0 17 13"><rect x="0" y="0" width="17" height="13" rx="1.5" fill="#ffffff"/><polyline points="1,1.5 8.5,7.5 16,1.5" fill="none" stroke="#444444" stroke-width="1.6"/></svg>
    <span class="footer-email">contact@tavrinel.com</span>
  </footer>
</body>
</html>
```